The name of the company is Harbor Turns buying foreclosed homes and remodeling

A sleek classy card. It’s a home remodel and house flip company. Something mostly black with dark gray and red in color . Something with two f”s as a logo on front as shown in pictures. Kind of just let you guys run with it . I left a few pictures that should help
You guys get an idea of what I thought was good also left all the information for back of the card

Target Market(s)

Home remodel consumers

Industry/Entity Type

Construction Company

Contact Information for Business Card

All details are on photo

Font styles to use
Decorative

Colors

Designer to choose colors to be used in the design.

Requirements
Must have
• Name of company on front. Harbor Turns
Nice to have
• Up to you guys I trust you
Should not have
• Not sure

```html
<!DOCTYPE html>
<html lang="en">
<head>
<meta charset="utf-8">
<title>Harbor Turns – Business Card</title>
<link rel="stylesheet" href="https://fonts.googleapis.com/css2?family=Oranienbaum&family=Open+Sans:wght@400&display=swap">
<style>
  :root {
    --ink: #000000;
    --charcoal: #3a3a3a;
    --paper: #ffffff;
    --red-bright: #d80d00;
    --red-deep: #560000;
    --icon-blue: #1f7fc0;
    --icon-red: #d9452f;
    --icon-pink: #c8327a;
    --text-dark: #111111;
  }
  html, body {
    margin: 0;
    padding: 0;
    overflow: hidden;
    background: #e9e9e9;
  }
  .card {
    position: relative;
    width: 1200px;
    height: 777px;
    background: var(--paper);
    overflow: hidden;
  }
  .card-shapes {
    position: absolute;
    inset: 0;
    width: 100%;
    height: 100%;
  }
  .owner-name {
    position: absolute;
    left: 26px;
    top: 26px;
    margin: 0;
    font-family: "Oranienbaum", serif;
    font-weight: 400;
    font-size: 66px;
    letter-spacing: 1px;
    color: var(--paper);
  }
  .contact-list {
    position: absolute;
    left: 222px;
    top: 220px;
    margin: 0;
    padding: 0;
    list-style: none;
    font-family: "Open Sans", sans-serif;
    font-size: 43px;
    color: var(--text-dark);
  }
  .contact-list li {
    height: 85px;
    line-height: 60px;
  }
  .service-list {
    position: absolute;
    margin: 0;
    padding: 0;
    list-style: none;
    font-family: "Oranienbaum", serif;
    font-size: 56px;
    color: var(--paper);
  }
  .service-list li {
    position: relative;
    height: 54px;
    line-height: 54px;
  }
  .service-list li::before {
    content: "";
    position: absolute;
    top: 20px;
    width: 25px;
    height: 25px;
    border-radius: 50%;
    background: var(--paper);
  }
  .services-left { left: 140px; top: 656px; }
  .services-left li::before { left: -47px; }
  .services-right { left: 639px; top: 656px; }
  .services-right li::before { left: -118px; }
</style>
</head>
<body>
<main class="card">
  <svg class="card-shapes" viewBox="0 0 1004 650" preserveAspectRatio="none" aria-hidden="true">
    <defs>
      <linearGradient id="band-top" x1="0" y1="0" x2="0" y2="1">
        <stop offset="0" stop-color="var(--charcoal)"/>
        <stop offset="0.55" stop-color="var(--ink)"/>
      </linearGradient>
      <linearGradient id="band-bottom" x1="0" y1="0" x2="0" y2="1">
        <stop offset="0.3" stop-color="var(--ink)"/>
        <stop offset="1" stop-color="var(--charcoal)"/>
      </linearGradient>
      <linearGradient id="accent-red" x1="0" y1="0" x2="1" y2="0">
        <stop offset="0" stop-color="var(--red-bright)"/>
        <stop offset="1" stop-color="var(--red-deep)"/>
      </linearGradient>
    </defs>

    <!-- top band -->
    <polygon points="0,0 1004,0 1004,90 220,128 0,137" fill="url(#band-top)"/>
    <polygon class="accent-top" points="220,128 1004,90 1004,125 940,193 855,158" fill="url(#accent-red)"/>

    <!-- bottom band -->
    <polygon class="accent-bottom" points="665,543 915,445 1004,470 1004,505" fill="url(#accent-red)"/>
    <polygon points="0,485 665,543 1004,503 1004,650 0,650" fill="url(#band-bottom)"/>

    <!-- divider -->
    <rect x="149" y="182" width="4" height="263" fill="var(--ink)"/>

    <!-- email marker -->
    <rect x="48" y="183" width="66" height="50" rx="4" fill="var(--icon-red)"/>
    <!-- social marker -->
    <circle cx="81" cy="272" r="31" fill="var(--icon-pink)"/>
    <!-- web globe -->
    <g fill="none" stroke="var(--icon-blue)" stroke-width="5">
      <circle cx="81" cy="340" r="32"/>
      <ellipse cx="81" cy="340" rx="14" ry="32"/>
      <line x1="81" y1="308" x2="81" y2="372"/>
      <line x1="49" y1="340" x2="113" y2="340"/>
      <path d="M55 322 Q81 330 107 322 M55 358 Q81 350 107 358"/>
    </g>
    <!-- phone -->
    <circle cx="81" cy="413" r="30" fill="none" stroke="var(--ink)" stroke-width="4"/>
    <path d="M68 398 l7 -3 l6 11 l-5 4 q3 8 10 13 l5 -4 l10 7 l-3 7 q-6 3 -14 -2 q-14 -10 -18 -24 q-2 -6 2 -9 z" fill="var(--ink)"/>
  </svg>

  <h1 class="owner-name">Daniel Whitcombe</h1>

  <ul class="contact-list">
    <li class="contact-email">DWhitcombeJR@mailbox.com</li>
    <li class="contact-social">_Harbor_Turns_</li>
    <li class="contact-web">www.HarborTurns.com</li>
    <li class="contact-phone">914-555-0173</li>
  </ul>

  <ul class="service-list services-left">
    <li>Brief Desc</li>
    <li>Home Remodel</li>
  </ul>
  <ul class="service-list services-right">
    <li>General Contractor</li>
    <li>Cocrete Alternative</li>
  </ul>
</main>
</body>
</html>
```